Lorvika.no is a new website about pedagogical entrepreneurship. It's main target group is teachers. The Fjellmark Institute for Classroom Media and the Nordvik Agency for Schools and Study are leading the project.

The web page is meant to show examples of how different methods of entrepreneurship can be used pedagogical in a learning environment. The page will also support the user with examples of different teaching programs and other examples of best practice.

Pedagogical entrepreneurship is not about business and men in suits. It's a method for learning. The focus in the design should be on school, education and new ways of learning.

The final product should be motivating and engaging, but at the same time governmental and serious. We are not looking for something "flashy" and corporate-looking, but a moderate, task-focused and clean design that state quality.

We need designs for three pages:
1 - frontpage
2 - subpage ("Metoder og undervisningsopplegg")
3 - subpage ("Smått-VERK i Brekkelia")

The interaction design for these three pages will be uploaded as an attachment.

We would like you to find inspiration in the following websites:
- www.gryvekst.no
- www.lavrek.no
- www.tovandstudio.com
- www.kvp.no
(more will be added)

Please use the attached logo, and feel free to use this as an inspiration for the rest of the design.

Target Market(s)

Teachers

Industry/Entity Type

Education

Requirements
Must have
• * Header with: Logo. Main navigation. Utility navigation. Search box.
* Footer
Should not have
• Images of men in suits.
Very strong graphical elements that stands out too much (we want it clean).

```html
<!DOCTYPE html>
<html lang="en">
<head>
<meta charset="utf-8">
<title>Lorvika – Methods and teaching plans</title>
<link rel="stylesheet" href="https://fonts.googleapis.com/css2?family=Arimo:ital,wght@0,400;0,700;1,700&display=swap">
<style>
:root{
  --ink:#222;
  --brand:#0e4d85;
  --brand-dark:#0a3d6b;
  --brand-mid:#1d6aa8;
  --callout:#1b7bc4;
  --band:#7fa1bd;
  --page:#eef0f2;
  --panel:#f4f4f5;
  --line:#cfd1d4;
  --nav:#0f4a80;
  --footer:#333333;
  --footer-base:#0c0c0c;
  --footer-text:#cfcfcf;
  --white:#ffffff;
}
*{box-sizing:border-box;margin:0;padding:0}
html,body{width:1028px;height:1200px;overflow:hidden}
body{position:relative;background:var(--page);font-family:"Arimo",Arial,sans-serif;color:var(--ink)}
.abs{position:absolute}

.top-strip{left:0;top:0;width:1028px;height:21px;background:#333}
.utility-tab{left:787px;top:0;width:160px;height:36px;background:#3a3a3a;clip-path:polygon(0 0,100% 0,100% 100%,6% 100%)}
.header{left:0;top:21px;width:1028px;height:79px;background:var(--white)}
.site-title{left:84px;top:30px;width:330px;text-align:center;font-style:italic;font-weight:700;font-size:25px;line-height:29px;color:var(--brand)}
.search-input{left:495px;top:36px;width:204px;height:21px;border:1px solid #aaa;background:#fff}
.search-btn{left:705px;top:35px;width:63px;height:23px;background:#2b2b2b;color:#fff;font-size:12px;line-height:23px;text-align:center}
.main-nav{left:391px;top:69px;width:556px;height:31px;background:var(--nav);display:flex;border-radius:4px 4px 0 0}
.main-nav a{flex:auto;color:#fff;text-decoration:none;font-size:12.5px;line-height:31px;text-align:center;border-left:1px solid #3a6e9e}
.main-nav a:first-child{border-left:0}
.header-rule{left:0;top:100px;width:1028px;height:5px;background:var(--brand)}
.band{left:0;top:105px;width:1028px;height:204px;background:var(--band)}

.container{left:81px;top:124px;width:866px;height:787px;background:var(--white);border-radius:5px 5px 0 0;box-shadow:0 0 8px rgba(0,0,0,.2)}
.hero{left:81px;top:124px;width:866px;height:133px;background:var(--brand);border-radius:5px 5px 0 0}
.brand{left:104px;top:158px;display:flex;align-items:center;gap:12px}
.brand-dot{width:40px;height:40px;border-radius:50%;background:#dde8f2}
.brand-name{font-size:36px;font-weight:700;color:#dde8f2;line-height:36px}
.brand-sub{left:176px;top:201px;font-size:8px;color:#cfe0ee}
.hero-tab{top:149px;width:171px;height:64px;background:var(--brand-dark);border:1px solid #2d6fa6;color:#fff;font-size:12px;line-height:15px;display:flex;align-items:center;justify-content:center;text-align:center;padding:0 14px}
.hero-tab.active{background:#6596bd;border-color:#9bbbd6}
.tab-pointer{left:636px;top:212px}

.box{left:99px;width:830px;background:#fff;border:1px solid var(--line);border-radius:4px;box-shadow:0 1px 2px rgba(0,0,0,.08)}
.methods-box{top:275px;height:189px}
.callout-shadow{left:112px;top:298px;width:213px;height:135px;background:linear-gradient(#fff,#e9eaec);box-shadow:0 2px 6px rgba(0,0,0,.15)}
.callout{left:124px;top:320px;width:187px;height:93px;background:var(--callout);border-radius:3px;color:#fff;font-size:11.5px;line-height:14.5px;padding:12px 12px}
.methods-panel{left:361px;top:297px;width:558px;height:156px;border:1px solid #bbb;border-radius:3px;background:#f7f7f8}
.panel-head{height:34px;background:linear-gradient(#f2f1f2,#d9d7d9);border-bottom:1px solid #bbb;display:flex;align-items:center;justify-content:space-between;padding:0 12px 0 14px}
.panel-title{font-weight:700;color:var(--brand);font-size:15px}
.toggle{width:24px;height:22px;background:#6b6b6b;border-radius:2px;display:flex;align-items:center;justify-content:center}
.method{width:164px;height:24px;border:1px solid #b9b9b9;background:linear-gradient(#fff,#eeeeee);font-size:10.5px;line-height:22px;padding-left:9px}

.plans-box{top:489px;height:396px}
.plans-head{left:99px;top:489px;width:830px;height:44px;background:linear-gradient(#f1f0f1,#d8d6d8);border-bottom:1px solid #c2c2c2;border-radius:4px 4px 0 0;display:flex;align-items:center;justify-content:space-between;padding:0 25px 0 23px}
.plans-title{font-weight:700;color:var(--brand);font-size:15px}
.plans-table{left:119px;top:549px;width:788px;height:323px;border:1px solid #c3c3c3;border-radius:3px;background:#e4e4e6}
.filter-row{left:127px;top:557px;width:772px;height:54px;background:linear-gradient(#fafafa,#e6e6e6)}
.filter-label{font-size:12px;color:#222}
.select{width:124px;height:25px;border:1px solid #8a8a8a;background:linear-gradient(#fff,#e7e7e7);font-size:12px;line-height:23px;padding-left:6px;border-radius:3px;overflow:hidden}
.select-arrow{position:absolute;right:0;top:0;width:25px;height:23px;background:linear-gradient(#3aa5d6,#1672a8);display:flex;align-items:center;justify-content:center}
.plan-row{left:127px;width:772px;height:37px;background:#fff;display:flex;font-size:12px;line-height:37px}
.plan-row span{border-right:2px solid #e4e4e6;padding-left:15px}
.plan-row span:last-child{border-right:0;padding-left:10px}
.c1{width:253px}.c2{width:159px}.c3{width:153px}.c4{flex:1}

.footer{left:0;top:911px;width:1028px;height:257px;background:var(--footer)}
.footer-rule{left:100px;top:944px;width:828px;height:1px;background:#4a4a4a}
.footer-mark{left:136px;top:995px;width:80px;height:80px;border-radius:50%;background:#4d4d4d}
.footer-name{left:136px;top:1084px;width:80px;text-align:center;font-size:13px;font-weight:700;color:#dcdcdc}
.footer-col h3{font-size:12px;font-weight:700;color:#fff;margin-bottom:20px}
.footer-col h4{font-size:10.5px;font-weight:700;color:#fff;margin:14px 0 12px}
.footer-col a{display:block;font-size:10.5px;color:var(--footer-text);text-decoration:none;margin-bottom:12px}
.footer-col a.more{color:#fff;text-decoration:underline;font-weight:700}
.footer-base{left:0;top:1168px;width:1028px;height:32px;background:var(--footer-base);color:#ddd;font-size:11.5px;line-height:32px;padding-left:325px}
</style>
</head>
<body>
<div class="abs top-strip"></div>
<div class="abs header"></div>
<div class="abs utility-tab"></div>
<div class="abs site-title">Enterprenerielle metoder<br>i undervisiningen</div>
<div class="abs search-input"></div>
<div class="abs search-btn">Search</div>
<nav class="abs main-nav">
  <a href="#">Home</a><a href="#">Why Lorvika</a><a href="#">Testimonials</a><a href="#">Methods</a><a href="#">News</a><a href="#">Blog</a><a href="#">Contact Us</a>
</nav>
<div class="abs header-rule"></div>
<div class="abs band"></div>

<div class="abs container"></div>
<div class="abs hero"></div>
<div class="abs brand"><span class="brand-dot"></span><span class="brand-name">Lorvika</span></div>
<div class="abs brand-sub">Entreprenerielle metoder i undervisningen</div>
<div class="abs hero-tab" style="left:387px">What is Pedagogical enterpreneurship?</div>
<div class="abs hero-tab active" style="left:567px">Methods and teaching plans</div>
<div class="abs hero-tab" style="left:752px">Good examples/<br>best practices</div>
<svg class="abs tab-pointer" width="34" height="33" viewBox="0 0 34 33"><polygon points="0,0 34,0 17,32" fill="#6596bd"/></svg>

<div class="abs box methods-box"></div>
<div class="abs callout-shadow"></div>
<div class="abs callout">Text about the methods and how they can be used. Also an intro to how teachers can find teaching resources.</div>
<svg class="abs" style="left:310px;top:355px" width="14" height="20" viewBox="0 0 14 20"><polygon points="0,0 13,10 0,20" fill="#1b7bc4"/></svg>
<div class="abs methods-panel">
  <div class="panel-head"><span class="panel-title">Methods</span>
    <span class="toggle"><svg width="10" height="7" viewBox="0 0 10 7"><polygon points="0,0 10,0 5,7" fill="#fff"/></svg></span></div>
</div>
<div class="abs method" style="left:379px;top:344px">Story line</div>
<div class="abs method" style="left:559px;top:344px">VERK</div>
<div class="abs method" style="left:741px;top:344px">Prosjektarbeid</div>
<div class="abs method" style="left:379px;top:376px">Elevbedriv/ungdomsbedrif</div>
<div class="abs method" style="left:559px;top:376px">Uteskole - Pedagogik</div>
<div class="abs method" style="left:741px;top:376px">Kreatif ekskursjoner</div>
<div class="abs method" style="left:379px;top:408px">Problembaserf laering</div>
<div class="abs method" style="left:559px;top:408px">Partnerskap</div>
<div class="abs method" style="left:741px;top:408px">Grunderkamp</div>

<div class="abs box plans-box"></div>
<div class="abs plans-head"><span class="plans-title">FIND TEACHING PLANS</span>
  <span class="toggle"><svg width="10" height="7" viewBox="0 0 10 7"><polygon points="0,0 10,0 5,7" fill="#fff"/></svg></span></div>
<div class="abs plans-table"></div>
<div class="abs filter-row"></div>
<div class="abs filter-label" style="left:142px;top:582px;font-size:13px">Tittle</div>
<div class="abs filter-label" style="left:380px;top:562px">Class/level</div>
<div class="abs filter-label" style="left:539px;top:562px">Time</div>
<div class="abs filter-label" style="left:692px;top:562px">Subject</div>
<div class="abs select" style="left:380px;top:579px">Alle<span class="select-arrow"><svg width="9" height="14" viewBox="0 0 9 14"><polygon points="0,6 9,6 4.5,0" fill="#111"/><polygon points="0,8 9,8 4.5,14" fill="#111"/></svg></span></div>
<div class="abs select" style="left:539px;top:579px">Alle<span class="select-arrow"><svg width="9" height="14" viewBox="0 0 9 14"><polygon points="0,6 9,6 4.5,0" fill="#111"/><polygon points="0,8 9,8 4.5,14" fill="#111"/></svg></span></div>
<div class="abs select" style="left:692px;top:579px">Alle<span class="select-arrow"><svg width="9" height="14" viewBox="0 0 9 14"><polygon points="0,6 9,6 4.5,0" fill="#111"/><polygon points="0,8 9,8 4.5,14" fill="#111"/></svg></span></div>

<div class="abs plan-row" style="top:621px"><span class="c1">Tittle</span><span class="c2">5 - 7&nbsp; level</span><span class="c3">2 weeks</span><span class="c4">Norwegian, Math, English</span></div>
<div class="abs plan-row" style="top:661px"><span class="c1">Tittle</span><span class="c2">5 - 7&nbsp; level</span><span class="c3">2 weeks</span><span class="c4">Norwegian, Math, English</span></div>
<div class="abs plan-row" style="top:701px"><span class="c1">Tittle</span><span class="c2">5 - 7&nbsp; level</span><span class="c3">2 weeks</span><span class="c4">Norwegian, Math, English</span></div>
<div class="abs plan-row" style="top:743px"><span class="c1">Tittle</span><span class="c2">5 - 7&nbsp; level</span><span class="c3">2 weeks</span><span class="c4">Norwegian, Math, English</span></div>
<div class="abs plan-row" style="top:784px"><span class="c1">Tittle</span><span class="c2">5 - 7&nbsp; level</span><span class="c3">2 weeks</span><span class="c4">Norwegian, Math, English</span></div>
<div class="abs plan-row" style="top:825px"><span class="c1">Tittle</span><span class="c2">5 - 7&nbsp; level</span><span class="c3">2 weeks</span><span class="c4">Norwegian, Math, English</span></div>

<footer>
  <div class="abs footer"></div>
  <div class="abs footer-rule"></div>
  <div class="abs footer-mark"></div>
  <div class="abs footer-name">Lorvika</div>
  <div class="abs footer-col" style="left:329px;top:922px">
    <h3>Pedagocical enterpreneurship</h3>
    <a href="#">What is Pedagogical enterpreneurship?</a>
    <a href="#">Science</a>
    <a href="#">Best practice school</a>
    <a href="#">Lorvikametere</a>
    <a href="#">About Lorvika.no</a>
  </div>
  <div class="abs footer-col" style="left:604px;top:922px">
    <h3>Methods</h3>
    <a href="#">Storyline</a>
    <a href="#">VERK</a>
    <a href="#">Cafe Pedagogikk</a>
    <a href="#" class="more">See more</a>
    <h4>Teaching Plans</h4>
    <a href="#">Tittle</a>
    <a href="#">Tittle</a>
    <a href="#" class="more">See more</a>
  </div>
  <div class="abs footer-col" style="left:753px;top:922px">
    <h3>Gode Eksemplar</h3>
    <a href="#">Smått-VERK at Brekkelia school</a>
    <a href="#">Smått-VERK at Brekkelia school</a>
    <a href="#">Smått-VERK at Brekkelia school</a>
    <a href="#" class="more">See more</a>
  </div>
  <div class="abs footer-base">Copyright &copy; 2012, Lorvika.com. All rights resreved.</div>
</footer>
</body>
</html>
```